Website Header / Banner needed

I need a new Header / Banner to be degigned to replace my current banner at http://www.velvorubtouch.example/banner334.gif

size is 713x 70 pixels (THIS IS THE CORRECT SIZE)

wording is slightly changed ie Velvo Massage 1000,s of UK Escorts & Massage Parlours

Target Market(s)

Adult

Industry/Entity Type

Adult

Logo Text

Velvo Massage 1000's of UK Escorts & Massage Parlours

Requirements
Must have
• size is 713x 70 pixels (THIS IS THE CORRECT SIZE)

```html
<!DOCTYPE html>
<html lang="en">
<head>
<meta charset="utf-8">
<title>Velvo Massage – Header Banner Options</title>
<link rel="stylesheet" href="https://fonts.googleapis.com/css2?family=Didact+Gothic&family=Arimo:wght@700&display=swap">
<style>
  :root {
    --backdrop: #c1cac9;
    --banner-bg: #ffffff;
    --banner-edge: #b7bfbe;
    --ink: #111111;
    --brand-red: #e3130f;
    --tone-light: #f1dccd;
    --tone-mid: #d9b29a;
    --tone-cool: #cfc8c4;
  }
  * { margin: 0; padding: 0; box-sizing: border-box; }
  html, body {
    width: 1200px;
    height: 600px;
    overflow: hidden;
    background: var(--backdrop);
  }
  .sheet {
    position: relative;
    width: 1200px;
    height: 600px;
  }
  .banner {
    position: absolute;
    left: 66px;
    width: 1070px;
    height: 105px;
    background: var(--banner-bg);
    border: 1px solid var(--banner-edge);
    overflow: hidden;
  }
  .banner--one { top: 82px; }
  .banner--two { top: 247px; }
  .banner--three { top: 415px; }

  .photo {
    position: absolute;
    top: 0;
    right: 0;
    width: 340px;
    height: 100%;
  }
  .photo--shoulder {
    background: linear-gradient(90deg, var(--banner-bg) 0%, var(--tone-light) 45%, var(--tone-mid) 100%);
  }
  .photo--stones {
    background: linear-gradient(90deg, var(--banner-bg) 0%, var(--tone-cool) 45%, var(--tone-mid) 100%);
  }
  .photo--face {
    background: linear-gradient(90deg, var(--banner-bg) 0%, var(--banner-bg) 20%, var(--tone-light) 60%, var(--tone-mid) 100%);
  }

  .brand-mark {
    position: absolute;
    left: 16px;
    top: 14px;
    width: 76px;
    height: 76px;
    border-radius: 50%;
    background: var(--brand-red);
  }
  .brand-name {
    position: absolute;
    left: 214px;
    top: 0;
    font-family: "Didact Gothic", "Century Gothic", sans-serif;
    font-size: 58px;
    font-weight: 400;
    letter-spacing: 3px;
    line-height: 1.05;
    color: var(--ink);
    white-space: nowrap;
  }
  .tagline {
    position: absolute;
    left: 138px;
    top: 67px;
    font-family: "Arimo", Arial, sans-serif;
    font-weight: 700;
    font-size: 24px;
    line-height: 1;
    letter-spacing: 1px;
    color: var(--ink);
    white-space: nowrap;
  }
</style>
</head>
<body>
<main class="sheet">
  <section class="banner banner--one">
    <div class="photo photo--shoulder" role="img" aria-label="Photo of a relaxed woman receiving a shoulder massage"></div>
    <span class="brand-mark" aria-hidden="true"></span>
    <h1 class="brand-name">Velvo Massage</h1>
    <p class="tagline">1000,s of UK Escorts &amp; Massage Parlours</p>
  </section>
  <section class="banner banner--two">
    <div class="photo photo--stones" role="img" aria-label="Photo of a woman resting on a towel in a spa setting"></div>
    <span class="brand-mark" aria-hidden="true"></span>
    <h2 class="brand-name">Velvo Massage</h2>
    <p class="tagline">1000,s of UK Escorts &amp; Massage Parlours</p>
  </section>
  <section class="banner banner--three">
    <div class="photo photo--face" role="img" aria-label="Photo of a woman receiving a gentle facial massage"></div>
    <span class="brand-mark" aria-hidden="true"></span>
    <h2 class="brand-name">Velvo Massage</h2>
    <p class="tagline">1000,s of UK Escorts &amp; Massage Parlours</p>
  </section>
</main>
</body>
</html>
```